skin elixir serum with snail extract

I am working at a natural skincare company. We are going to launch a new product - a skin serum. completely natural, super concentrated, multi use (face, neck , eyes). But we need the packaging (box and bottle label) to be aligned to our brand's philosophy, design etc. (See more at pindomare.com)

Here's a more detailed description :
"Elevate your skincare routine with Brusquel Elixir, the ultimate one-drop wonder enriched with potent snail secretion. Experience the magic as our 100% natural serum transforms your face, eyes, décolleté, and neck. Get ready to say Wow to a new level of radiance!"

Target Market(s)

natural skincare enthusiasts - beauty pioneers

Industry/Entity Type

beauty - wellness

Requirements
Nice to have
• based on the overall brand philosophy (see pindomare.com)

```html
<!DOCTYPE html>
<html lang="en">
<head>
<meta charset="utf-8">
<title>Pindomare – Brusquel Elixir packaging</title>
<link rel="stylesheet" href="https://fonts.googleapis.com/css2?family=Poppins:ital,wght@0,200;0,300;0,400;0,600;1,300&display=swap">
<style>
  :root {
    --backdrop: #e8e8e8;
    --coral: #e06a74;
    --coral-soft: #ef9aa0;
    --rose: #c88d90;
    --label-white: #fbfbfb;
    --carton-grey: #e9e9e9;
    --wood-light: #d9a56a;
    --wood-dark: #a86f36;
    --ink-white: #ffffff;
  }
  * { box-sizing: border-box; margin: 0; padding: 0; }
  html, body { width: 1200px; height: 800px; overflow: hidden; }
  body {
    background: var(--backdrop);
    font-family: "Poppins", sans-serif;
    color: var(--coral);
    position: relative;
  }

  /* ---------- Bottle ---------- */
  .bottle { position: absolute; left: 150px; top: 40px; width: 210px; height: 720px; }
  .bottle__cap {
    height: 130px; border-radius: 18px 18px 4px 4px;
    background: linear-gradient(90deg, var(--wood-dark), var(--wood-light) 45%, var(--wood-dark));
  }
  .bottle__label {
    height: 590px; background: var(--label-white);
    border-radius: 0 0 14px 14px;
    padding: 28px 18px 0; text-align: center;
    display: flex; flex-direction: column; align-items: center;
  }
  .brand-name { font-weight: 400; color: var(--coral); letter-spacing: 0.5px; }
  .bottle .brand-name { font-size: 26px; }
  .tagline { font-weight: 300; font-size: 10px; line-height: 1.35; margin-top: 6px; }
  .product-name { margin-top: 30px; font-weight: 200; line-height: 1; }
  .product-name__main { display: block; font-size: 30px; letter-spacing: 3px; }
  .product-name__sub { display: block; font-size: 13px; letter-spacing: 6px; margin-top: 6px; }
  .snail-mark { width: 34px; height: 26px; margin-top: 22px; border-radius: 50%; background: var(--coral); }
  .copy { font-size: 9.5px; font-weight: 300; line-height: 1.4; margin-top: 14px; max-width: 160px; }
  .copy strong { font-weight: 600; }
  .copy--first { margin-top: 12px; }
  .shell-band {
    margin-top: auto; margin-bottom: 24px; width: 160px; height: 60px; border-radius: 8px;
    background: linear-gradient(90deg, var(--coral-soft), var(--coral), var(--coral-soft));
  }

  /* ---------- Carton ---------- */
  .carton { position: absolute; top: 70px; left: 470px; display: flex; gap: 0; }
  .carton__face { height: 660px; width: 260px; display: flex; flex-direction: column; align-items: center; text-align: center; padding: 36px 22px 0; }
  .carton__front { background: var(--carton-grey); }
  .carton__front .brand-name { font-size: 34px; }
  .carton__front .tagline { font-size: 12px; }
  .carton__front .product-name__main { font-size: 34px; }
  .carton__front .copy { font-size: 10.5px; max-width: 190px; }
  .carton__front .shell-band { width: 200px; height: 80px; }

  .carton__side { background: var(--rose); color: var(--ink-white); }
  .carton__side .brand-name { color: var(--ink-white); font-size: 34px; }
  .carton__side .tagline { font-style: italic; font-size: 12px; }
  .claims { display: grid; grid-template-columns: repeat(2, 64px); gap: 14px 26px; margin-top: 26px; justify-content: center; }
  .claim { display: flex; flex-direction: column; align-items: center; font-size: 7px; font-weight: 300; }
  .claim svg { width: 44px; height: 44px; }
  .claim--solo { grid-column: 1 / span 2; }
  .usage { font-size: 8.5px; font-style: italic; font-weight: 300; line-height: 1.5; margin-top: 20px; max-width: 190px; }
  .carton__side .shell-band { width: 200px; height: 60px; background: linear-gradient(90deg, var(--coral-soft), var(--coral), var(--coral-soft)); }

  .carton__top {
    position: absolute; left: 540px; top: 0; width: 180px; height: 150px;
    background: var(--carton-grey); display: flex; flex-direction: column; align-items: center; justify-content: center; text-align: center;
  }
  .carton__top .brand-name { font-size: 22px; }
  .carton__top .tagline { font-size: 7px; margin-top: 2px; }
  .carton__top .product-name { margin-top: 8px; }
  .carton__top .product-name__main { font-size: 14px; letter-spacing: 2px; }
  .carton__top .product-name__sub { font-size: 7px; letter-spacing: 4px; margin-top: 2px; }
</style>
</head>
<body>

<section class="bottle">
  <div class="bottle__cap" role="img" aria-label="Natural wooden bottle cap"></div>
  <div class="bottle__label">
    <p class="brand-name">Pindomare</p>
    <p class="tagline">Elevate your skincare<br>routine with</p>
    <h1 class="product-name"><span class="product-name__main">BRUSQUEL</span><span class="product-name__sub">ELIXIR</span></h1>
    <div class="snail-mark" role="img" aria-label="Small snail illustration"></div>
    <p class="copy">The ultimate one-drop wonder enriched with potent snail secretion</p>
    <p class="copy">Experience the magic as our <strong>100% natural</strong> serum</p>
    <p class="copy"><strong>Transforms your face, eyes, décolleté, and neck.</strong></p>
    <p class="copy">Get ready to say WOW to a new level of radiance!</p>
    <div class="shell-band" role="img" aria-label="Decorative band of spiral snail shells"></div>
  </div>
</section>

<section class="carton">
  <div class="carton__face carton__front">
    <p class="brand-name">Pindomare</p>
    <p class="tagline">Elevate your skincare<br>routine with</p>
    <h2 class="product-name"><span class="product-name__main">BRUSQUEL</span><span class="product-name__sub">ELIXIR</span></h2>
    <p class="copy copy--first">The ultimate one-drop wonder enriched with potent snail secretion</p>
    <p class="copy">Experience the magic as our <strong>100% natural</strong> serum</p>
    <p class="copy"><strong>Transforms your face, eyes, décolleté, and neck.</strong></p>
    <p class="copy">Get ready to say WOW to a new level of radiance!</p>
    <div class="shell-band" role="img" aria-label="Decorative band of spiral snail shells"></div>
  </div>

  <div class="carton__face carton__side">
    <p class="brand-name">Pindomare</p>
    <p class="tagline">Elevate your skincare<br>routine with</p>
    <div class="claims">
      <div class="claim">
        <svg viewBox="0 0 44 44" fill="none" stroke="#fff" stroke-width="1"><circle cx="22" cy="22" r="20"/><circle cx="22" cy="22" r="10"/><path d="M12 22h20M22 12c-5 6-5 14 0 20M22 12c5 6 5 14 0 20"/></svg>
        <span>eco-friendly</span>
      </div>
      <div class="claim">
        <svg viewBox="0 0 44 44" fill="none" stroke="#fff" stroke-width="1"><circle cx="22" cy="22" r="20"/><path d="M22 11c8 6 8 16 0 22c-8-6-8-16 0-22zM22 14v19"/></svg>
        <span>100% natural</span>
      </div>
      <div class="claim">
        <svg viewBox="0 0 44 44" fill="none" stroke="#fff" stroke-width="1"><circle cx="22" cy="22" r="20"/><path d="M22 11c5 7 8 11 8 15a8 8 0 0 1-16 0c0-4 3-8 8-15z"/></svg>
        <span>gluten-free</span>
      </div>
      <div class="claim">
        <svg viewBox="0 0 44 44" fill="none" stroke="#fff" stroke-width="1"><circle cx="22" cy="22" r="20"/><path d="M13 30c0-10 8-17 18-17c0 10-7 17-18 17zM13 30l12-11"/></svg>
        <span>vegan</span>
      </div>
      <div class="claim claim--solo">
        <svg viewBox="0 0 44 44" fill="none" stroke="#fff" stroke-width="1"><circle cx="22" cy="22" r="20"/><path d="M22 11c7 6 7 16 0 22c-7-6-7-16 0-22z"/></svg>
        <span>derma tested</span>
      </div>
    </div>
    <p class="usage">Apply one drop to clean skin morning and evening. Warm between fingertips and press gently onto face, eyes, neck and décolleté. Made with carefully filtered snail secretion and plant extracts. Store in a cool, dry place away from direct sunlight. For external use only. Avoid direct contact with eyes. Keep out of reach of children.</p>
    <div class="shell-band" role="img" aria-label="Decorative band of spiral snail shells"></div>
  </div>

  <div class="carton__face carton__top">
    <p class="brand-name">Pindomare</p>
    <p class="tagline">Elevate your skincare routine with</p>
    <p class="product-name"><span class="product-name__main">BRUSQUEL</span><span class="product-name__sub">ELIXIR</span></p>
  </div>
</section>

</body>
</html>
```